looking for sleek business card to standout from the crowd!

We are a young biotechnology company looking to help you personalize your health through understanding your genetic make up. We need you help in making a clean but sleek business card design using our new logo. The goal? Any time we give our cards out, people say "nice card!" The feel we are going for is "modern-techy". We don't want to come across as an old, giant pharma company, but not trying to be a hipster either.

Target Market(s)

healthcare and biotechnology industry.

Industry/Entity Type

Biotechnology

Contact Information for Business Card

Info to include on the card will be NAME, TITLE, EMAIL, PHONE. The companies website (www.corvalinbio.com) should also be on the card some where. Would like the logo, when printed, to be raised.

Requirements
Must have
• The logo we have attached in the color it is in. Fonts for text should lean toward more professional/tech.
Nice to have
• Prefer white/light color background
Should not have
• cartoons, landscape backgrounds images.

```html
<!DOCTYPE html>
<html lang="en">
<head>
<meta charset="utf-8">
<title>Corvalin Business Card</title>
<link href="https://fonts.googleapis.com/css2?family=Source+Sans+3:wght@400;700&display=swap" rel="stylesheet">
<style>
  :root {
    --page-bg: #dde5e8;
    --card-white: #ffffff;
    --wave-blue: #00aeef;
    --wave-slate: #527f8e;
    --brand-blue: #1170b8;
    --text-light: #ffffff;
  }
  * { margin: 0; padding: 0; box-sizing: border-box; }
  html, body {
    width: 1200px;
    height: 1000px;
    overflow: hidden;
    background: var(--page-bg);
    font-family: "Source Sans 3", Arial, sans-serif;
  }
  .business-card {
    position: absolute;
    left: 100px;
    top: 200px;
    width: 1000px;
    height: 600px;
    background: var(--card-white);
    overflow: hidden;
  }
  .card-wave {
    position: absolute;
    inset: 0;
    width: 1000px;
    height: 600px;
  }
  .wave-band { fill: var(--wave-slate); }
  .wave-fill { fill: var(--wave-blue); }
  .brand-name {
    position: absolute;
    left: 90px;
    top: 112px;
    font-weight: 700;
    font-size: 104px;
    line-height: 1;
    letter-spacing: 2px;
    color: var(--brand-blue);
  }
  .holder {
    position: absolute;
    right: 86px;
    top: 318px;
    text-align: right;
    color: var(--text-light);
  }
  .holder-name {
    font-size: 40px;
    font-weight: 400;
    line-height: 1.1;
  }
  .holder-title {
    font-size: 26px;
    line-height: 1.2;
  }
  .contact-list {
    position: absolute;
    left: 296px;
    top: 424px;
    display: grid;
    grid-template-columns: 190px auto;
    column-gap: 18px;
    row-gap: 3px;
    color: var(--text-light);
    font-size: 27px;
    line-height: 1.25;
  }
  .contact-label { text-align: right; }
</style>
</head>
<body>
  <div class="business-card">
    <svg class="card-wave" viewBox="0 0 1000 600" aria-hidden="true">
      <path class="wave-band" d="M0,345 C120,440 240,470 380,420 C560,355 760,210 1000,212 V600 H0 Z"/>
      <path class="wave-fill" d="M0,358 C125,452 250,482 390,432 C570,368 780,290 1000,300 V600 H0 Z"/>
    </svg>

    <span class="brand-name">CORVALIN</span>

    <div class="holder">
      <p class="holder-name">Proprietor's Name</p>
      <p class="holder-title">Your Title</p>
    </div>

    <div class="contact-list">
      <span class="contact-label">Mobile :</span>
      <span class="contact-value">+123 456 789</span>
      <span class="contact-label">Email :</span>
      <span class="contact-value">yourname@email.com</span>
      <span class="contact-label">Web :</span>
      <span class="contact-value">www.corvalinbio.com</span>
    </div>
  </div>
</body>
</html>
```